Asian-oriented Soya Desert Logo and Packaging/Label

We need a logo and packaging design for a new Soya Dessert business based in London called '云雀糖 Soya Desserts'. The name essentially means Tofu Boy - but this doesn't mean the design needs to revolve around a boy.

We produce a wide variety of flavoured Soya Desserts made from the highest quality organic soya beans. Our flavours are exotic, colourful and refreshing - think of flavours such as Honeydew (Green colour), Mango (Orange colour), Taro (Purple Colour) etc. The packaging design should allow the option to have a different colour for each flavour.

Our main target market are Chinese and we will sell our products through Asian Supermarkets and Restaurants.

We would like the design to give off an image which is young, colourful and whimsical, yet a company which has Chinese roots, hence the Chinese name despite being a UK company.

We have included the packaging that the product will come in. It's essentially a clear plastic pot with a lid. We would ideally like to have the top labelled and a bit of the sides - it's preferable to allow the consumers to see the actual dessert, hence we would prefer not to cover up all of the sides.

Package Dimensions: Please see the attached image which should give you the diameter in millimetres. If you require any other dimensions, please let me know. The shape is conical, and not a cylinder, so the upper and lower dimensions are different.

Nutritional Information: The product is still going through Group 2 nutritional testing, so I don't have this info yet. Please just use a blank 'Group 2 Nutrition Label' for now.

Target Market(s)

Asians/Chinese

Industry/Entity Type

Business

Logo Text

云雀糖 Soya Desserts

Requirements
Must have
• - Nutrition Label
• - Ingredients Label
• - Net Weight: ℮ 330g
• Please ensure you state the below on the packaging:
• - Must Keep Refrigerated
• - Use by date:
• And these wording in 3 different languages (please see link in one of the images)
• - Produced with Non-GMO Soya Beans
• - No Gypsum Powder

```html
<!DOCTYPE html>
<html lang="en">
<head>
<meta charset="utf-8">
<title>云雀糖 Soya Desserts – Mango lid label</title>
<link rel="stylesheet" href="https://fonts.googleapis.com/css2?family=Aladin&family=Noto+Serif+SC:wght@700&family=Noto+Serif:wght@700&display=swap">
<style>
  :root {
    --paper: #ffffff;
    --rim: #1a1a1a;
    --flavour: #f7941d;
    --vine: #8dc63f;
    --blossom: #f26522;
    --brand: #e6007e;
    --brand-dot: #8dc63f;
    --ink: #111111;
  }
  html, body {
    margin: 0;
    padding: 0;
    width: 1200px;
    height: 1200px;
    overflow: hidden;
    background: var(--paper);
  }
  .label {
    position: relative;
    width: 1200px;
    height: 1200px;
  }
  .label-art {
    position: absolute;
    inset: 0;
  }
  .brand {
    position: absolute;
    left: 566px;
    top: 512px;
    display: flex;
    align-items: center;
    gap: 14px;
    color: var(--brand);
    font-family: "Noto Serif SC", "Noto Serif", serif;
    font-weight: 700;
    font-size: 40px;
    line-height: 1;
    white-space: nowrap;
  }
  .brand-name small {
    display: block;
    font-size: 22px;
    margin-top: 4px;
  }
  .brand-dot {
    width: 62px;
    height: 62px;
    border-radius: 50%;
    background: var(--brand-dot);
  }
  .flavour-name {
    position: absolute;
    left: 480px;
    top: 590px;
    margin: 0;
    color: var(--flavour);
    font-family: "Aladin", cursive;
    font-weight: 400;
    font-size: 160px;
    line-height: 1;
    letter-spacing: 4px;
  }
  .sell-by {
    position: absolute;
    left: 506px;
    top: 1000px;
    margin: 0;
    color: var(--ink);
    font-family: "Noto Serif", serif;
    font-weight: 700;
    font-size: 16px;
  }
</style>
</head>
<body>
<main class="label">
  <svg class="label-art" width="1200" height="1200" viewBox="0 0 1200 1200">
    <defs>
      <linearGradient id="vine-tone" x1="0" y1="0" x2="1" y2="1">
        <stop offset="0" stop-color="#b5dd7a"/>
        <stop offset="0.5" stop-color="#f7b267"/>
        <stop offset="1" stop-color="#a9d86a"/>
      </linearGradient>
      <linearGradient id="lantern-tone" x1="0" y1="0" x2="0" y2="1">
        <stop offset="0" stop-color="#f9a04a"/>
        <stop offset="1" stop-color="#f26522"/>
      </linearGradient>
    </defs>
    <circle class="outer-rim" cx="600" cy="600" r="478" fill="none" stroke="var(--rim)" stroke-width="3"/>
    <circle class="flavour-ring" cx="600" cy="600" r="448" fill="none" stroke="var(--flavour)" stroke-width="6"/>
    <path class="wreath" role="img" aria-label="Crescent wreath of green blossom branches with orange and red flowers"
          d="M 846 435 A 330 330 0 1 0 830 790"
          fill="none" stroke="url(#vine-tone)" stroke-width="96" stroke-linecap="round" opacity="0.85"/>
    <g class="lanterns" role="img" aria-label="Two hanging orange paper lanterns">
      <rect x="534" y="388" width="58" height="84" rx="26" fill="url(#lantern-tone)"/>
      <rect x="456" y="460" width="92" height="100" rx="40" fill="url(#lantern-tone)"/>
    </g>
  </svg>

  <div class="brand">
    <span class="brand-name">云雀糖<small>Soya Desserts</small></span>
    <span class="brand-dot"></span>
  </div>

  <h1 class="flavour-name">Mango</h1>

  <p class="sell-by">Sell by: Dec 22 2017</p>
</main>
</body>
</html>
```